Referring Dentists Referral Card

Corwell Pediatric & Teen Dentistry is looking for a new referral card to give to dentists sending their patients to our office for special treatment. Corwell Pediatric & Teen Dentistry is a modern, fun, and safe environment for children and teens to receive and experience the highest quality of dental care available. At CPTD we believe in shaping a positive experience for your child so they look forward to and love coming to the dentist!

Target Market(s)

Dentists

Industry/Entity Type

Dental

Font styles to use
Sans Serif

Colors
0292cd
acd036
f37122

Requirements
Must have
• Logo, phone number, copy from file "Referral Card In"

```html
<!DOCTYPE html>
<html lang="en">
<head>
<meta charset="utf-8">
<title>Corwell Pediatric &amp; Teen Dentistry – Referral Card</title>
<link href="https://fonts.googleapis.com/css2?family=Arimo:wght@400&family=Cabin:wght@400&display=swap" rel="stylesheet">
<style>
  :root {
    --orange: #e95d22;
    --brand-orange: #f37122;
    --blue: #0292cd;
    --green: #7dbb45;
    --box-green: #3fae49;
    --ink: #2b2b2b;
    --grey: #a6a6a6;
    --rule: #b5b5b5;
    --paper: #fdfdfd;
  }
  * { margin: 0; padding: 0; box-sizing: border-box; }
  html, body { width: 1062px; height: 1200px; overflow: hidden; background: var(--paper); }
  body { font-family: "Arimo", Arial, sans-serif; color: var(--ink); }
  .card { position: relative; width: 1062px; height: 1200px; background: var(--paper); }
  .crop-marks { position: absolute; inset: 0; }
  .side-band { position: absolute; left: 17px; top: 17px; width: 106px; height: 1165px; background: var(--orange); }

  .brand { position: absolute; left: 184px; top: 91px; display: flex; align-items: center; gap: 14px; }
  .brand-square { width: 107px; height: 108px; background: var(--brand-orange); }
  .brand-name { font-size: 34px; line-height: 1.1; color: var(--ink); }

  .reminder { position: absolute; left: 704px; top: 85px; border-left: 7px solid var(--grey); padding-left: 10px;
    font-size: 24px; line-height: 28px; color: var(--grey); }

  .pointer { position: absolute; left: 123px; top: 242px; }
  .intro { position: absolute; left: 184px; top: 246px; font-size: 28px; line-height: 33px; color: var(--blue); }

  .notice { position: absolute; left: 184px; top: 371px; width: 861px; height: 46px; background: var(--green);
    font-family: "Cabin", sans-serif; font-size: 29px; color: #fff; line-height: 46px; padding-left: 20px; letter-spacing: 0.3px; }

  .option { position: absolute; display: flex; align-items: center; }
  .box { width: 28px; height: 28px; border: 2px solid var(--box-green); background: #fff; flex: none; }
  .doctor { left: 184px; font-size: 27px; }
  .doctor .box { margin-right: 48px; }
  .reason { left: 244px; font-size: 26px; }
  .reason .box { margin-right: 10px; }

  .field { position: absolute; left: 151px; font-size: 26px; display: flex; align-items: flex-end; }
  .field .rule { flex: 1; border-bottom: 2px solid var(--rule); margin-left: 6px; margin-bottom: 5px; }
  .rule-line { position: absolute; left: 154px; width: 812px; border-top: 2px solid var(--rule); }
</style>
</head>
<body>
<main class="card">
  <svg class="crop-marks" width="1062" height="1200" aria-hidden="true">
    <g stroke="#222" stroke-width="2">
      <line x1="50" y1="0" x2="50" y2="16"/><line x1="1012" y1="0" x2="1012" y2="16"/>
      <line x1="0" y1="50" x2="14" y2="50"/><line x1="1048" y1="50" x2="1062" y2="50"/>
      <line x1="50" y1="1184" x2="50" y2="1200"/><line x1="1012" y1="1184" x2="1012" y2="1200"/>
      <line x1="0" y1="1147" x2="14" y2="1147"/><line x1="1048" y1="1147" x2="1062" y2="1147"/>
    </g>
  </svg>

  <div class="side-band"></div>

  <div class="brand">
    <div class="brand-square"></div>
    <div class="brand-name">Corwell Pediatric<br>&amp; Teen Dentistry</div>
  </div>

  <p class="reminder">Please bring this form<br>to your appointment</p>

  <svg class="pointer" width="46" height="53" aria-hidden="true"><polygon points="0,0 46,26.5 0,53" fill="var(--blue)"/></svg>
  <p class="intro">Your dentist cares for the well being of your child<br>by referring to the pediatric dental specialists at<br>Corwell Pediatric &amp; Teen Dentistry.</p>

  <div class="notice">Our Office does not provide oral conscious sedation</div>

  <div class="option doctor" style="top:442px"><span class="box"></span>Harlan Westbrook, DDSMSD</div>
  <div class="option doctor" style="top:489px"><span class="box"></span>Derek Oakridge, DDS</div>

  <div class="field" style="top:642px; width:813px">Patient Name<span class="rule"></span></div>
  <div class="field" style="top:704px; width:816px">Referring Doctor<span class="rule"></span></div>

  <div class="option reason" style="top:762px"><span class="box"></span>Consultation for General Anesthesia</div>
  <div class="option reason" style="top:802px"><span class="box"></span>Complex dental needs</div>
  <div class="option reason" style="top:843px"><span class="box"></span>Dental anxiety</div>

  <div class="field" style="top:900px; width:815px">Comments<span class="rule"></span></div>
  <div class="rule-line" style="top:968px"></div>
  <div class="rule-line" style="top:1016px"></div>
  <div class="rule-line" style="top:1065px"></div>
  <div class="rule-line" style="top:1113px"></div>
</main>
</body>
</html>
```